Business Card Design - Corporate

Create a sleek elegant business card layout while suggesting a color scheme. Convey cutting edge technology while maintaining a corporate feel that is easily readable.

Company designs and manufactures consumer electronic products for mass retail that are mainly app driven.

(vector logo and die-line provided)

Target Market(s)

Corporate level, tech industry.

Industry/Entity Type

Business

Contact Information for Business Card

Generic Info:

Name
Title
email
address
phone 1
phone 2
website (vantorelle.com) on back

Font styles to use
Sans Serif

Requirements
Must have
• At least 2 colors + white on one side.
Nice to have
• Solid suggestion on color for logo and overall design. Color flood on back of card.
Should not have
• background texture like... marble, stone, patterns or circuit boards

```html
<!DOCTYPE html>
<html lang="en">
<head>
<meta charset="utf-8">
<title>Vantorelle Business Card</title>
<link href="https://fonts.googleapis.com/css2?family=Open+Sans:wght@400;600;700&display=swap" rel="stylesheet">
<style>
  :root {
    --brand-blue: #0b72bf;
    --brand-blue-deep: #0a66ad;
    --ink: #3c3f45;
    --ink-soft: #6b6f76;
    --card-white: #f4f7fb;
    --page: #e6e8eb;
  }
  * { margin: 0; padding: 0; box-sizing: border-box; }
  html, body {
    width: 1200px;
    height: 880px;
    overflow: hidden;
    background: var(--page);
    font-family: "Open Sans", sans-serif;
  }
  .stage {
    width: 1200px;
    height: 880px;
    display: flex;
    align-items: center;
    justify-content: center;
    gap: 40px;
  }
  .card {
    position: relative;
    width: 540px;
    height: 310px;
    overflow: hidden;
    box-shadow: 0 6px 18px rgba(0,0,0,0.18);
  }
  .wordmark {
    font-family: "Open Sans", sans-serif;
    font-weight: 600;
    text-transform: uppercase;
    line-height: 1;
  }

  /* Back */
  .card--back {
    background: var(--brand-blue);
    display: flex;
    align-items: center;
    justify-content: center;
  }
  .card--back .wordmark {
    color: #ffffff;
    font-size: 40px;
    letter-spacing: 5px;
  }

  /* Front */
  .card--front { background: var(--card-white); }
  .card--front .wordmark {
    position: absolute;
    left: 34px;
    top: 100px;
    color: var(--ink);
    font-size: 31px;
    letter-spacing: 3px;
  }
  .holder {
    position: absolute;
    right: 30px;
    top: 58px;
    text-align: right;
  }
  .holder-name {
    color: var(--brand-blue);
    font-weight: 700;
    font-size: 19px;
    line-height: 24px;
    letter-spacing: 0.3px;
  }
  .holder-title {
    color: var(--ink);
    font-size: 11px;
    line-height: 16px;
    margin-top: 2px;
  }
  .holder-meta {
    margin-top: 18px;
    color: var(--ink-soft);
    font-size: 10.5px;
    line-height: 1.6;
  }
  .contact-list {
    position: absolute;
    left: 34px;
    top: 188px;
    list-style: none;
  }
  .contact-item {
    display: flex;
    align-items: center;
    gap: 8px;
    color: var(--ink);
    font-size: 16px;
    line-height: 22px;
  }
  .contact-item svg { width: 12px; height: 12px; flex: none; }
  .license-band {
    position: absolute;
    left: 0; right: 0; bottom: 0;
    height: 46px;
    background: var(--brand-blue-deep);
    color: #ffffff;
    font-size: 12px;
    letter-spacing: 0.4px;
    display: flex;
    align-items: center;
    justify-content: center;
  }
</style>
</head>
<body>
<main class="stage">
  <section class="card card--back" aria-label="Card back">
    <span class="wordmark">Vantorelle</span>
  </section>

  <section class="card card--front" aria-label="Card front">
    <span class="wordmark">Vantorelle</span>

    <div class="holder">
      <p class="holder-name">ARLEN VOSS</p>
      <p class="holder-title">Managing Director</p>
      <p class="holder-meta">Mob : 0400 555 217<br>ABN : 51 730 264 918<br>14 Harbour Lane, Sydney NSW 2000</p>
    </div>

    <ul class="contact-list">
      <li class="contact-item">
        <svg viewBox="0 0 12 12" aria-hidden="true"><path fill="#0b72bf" d="M2.4 0.8l1.8 0.2 0.8 2.4-1.2 1a6.5 6.5 0 0 0 3 3l1-1.2 2.4 0.8 0.2 1.8-1.4 1.2C5.6 10 2 6.4 1.2 2.2z"/></svg>
        +91-555-010-0447
      </li>
      <li class="contact-item">
        <svg viewBox="0 0 12 12" aria-hidden="true"><g fill="none" stroke="#0b72bf" stroke-width="1.2"><circle cx="6" cy="6" r="5"/><ellipse cx="6" cy="6" rx="2.2" ry="5"/><path d="M1 6h10"/></g></svg>
        vantorelle.com
      </li>
      <li class="contact-item">
        <svg viewBox="0 0 12 12" aria-hidden="true"><rect x="0.5" y="2" width="11" height="8" fill="#0b72bf"/><path d="M0.8 2.4L6 6.6l5.2-4.2" fill="none" stroke="#fff" stroke-width="1"/></svg>
        arlen@vantorelle.com
      </li>
    </ul>

    <div class="license-band">Lic No : L052718 / AU30461</div>
  </section>
</main>
</body>
</html>
```